Business Card Design - Cryotherapy

We need a custom created business card for our company FrostLume Spa. We provide whole body cryotherapy and localized cryotherapy to our clients. Please be creative.
Please see our website for idea's on design.
www.frostlumespa.com
Industry/Entity Type
Business
Contact Information for Business Card
Name, Position, Phone Number, Address, Website, Email
Look and feel
Each slider illustrates characteristics of the customer's brand and the style your logo design should communicate.

```html
<!DOCTYPE html>
<html lang="en">
<head>
<meta charset="utf-8">
<title>FrostLume Spa – Business Card</title>
<link href="https://fonts.googleapis.com/css2?family=Roboto:wght@400;500&display=swap" rel="stylesheet">
<style>
  :root {
    --bg: #a9a7a8;
    --card: #fbfbfb;
    --green: #1a7f4e;
    --teal: #17a3b5;
    --teal-dark: #0f8f92;
    --ink: #3a3a3a;
    --muted: #555;
    --ghost: #ececec;
  }
  * { margin: 0; padding: 0; box-sizing: border-box; }
  html, body { width: 1200px; height: 1200px; overflow: hidden; }
  body {
    background: var(--bg);
    position: relative;
    font-family: "Roboto", sans-serif;
  }
  .card {
    position: absolute;
    background: var(--card);
    border-radius: 22px;
    overflow: hidden;
  }
  .card--front { left: 238px; top: 120px; width: 712px; height: 417px; }
  .card--back  { left: 231px; top: 645px; width: 711px; height: 417px; }

  .ghost-mark {
    position: absolute;
    left: 380px; top: 30px;
    width: 360px; height: 360px;
    border-radius: 50%;
    background: var(--ghost);
  }
  .brand {
    position: absolute;
    display: flex;
    align-items: center;
    gap: 18px;
  }
  .brand__dot {
    border-radius: 50%;
    background: var(--teal);
    flex: none;
  }
  .brand__name {
    color: var(--green);
    font-weight: 500;
    white-space: nowrap;
  }
  .card--front .brand { left: 118px; top: 145px; }
  .card--front .brand__dot { width: 76px; height: 76px; }
  .card--front .brand__name { font-size: 56px; }
  .card--back .brand { left: 40px; top: 42px; }
  .card--back .brand__dot { width: 68px; height: 68px; }
  .card--back .brand__name { font-size: 48px; }

  .wave { position: absolute; left: 0; top: 0; }
  .footer-band { position: absolute; left: 0; bottom: 0; }

  .person { position: absolute; left: 46px; top: 218px; }
  .person__name { color: var(--green); font-size: 26px; font-weight: 400; }
  .person__title { color: var(--muted); font-size: 16px; margin-top: 4px; }

  .contact { position: absolute; left: 344px; top: 208px; color: var(--ink); font-size: 19px; }
  .contact__row { display: flex; align-items: center; height: 27.5px; }
  .contact__icon { width: 18px; height: 18px; margin-right: 17px; fill: var(--teal); }
  .contact__address { margin-top: 9px; line-height: 25px; }
</style>
</head>
<body>

  <section class="card card--front">
    <div class="ghost-mark" aria-hidden="true"></div>
    <div class="brand">
      <span class="brand__dot"></span>
      <span class="brand__name">FrostLume Spa</span>
    </div>
  </section>

  <section class="card card--back">
    <svg class="wave" width="711" height="60" viewBox="0 0 711 60" aria-hidden="true">
      <path d="M185 0 H711 V40 C600 10 460 22 330 14 C270 10 225 5 185 0 Z" fill="var(--teal-dark)"/>
    </svg>

    <div class="brand">
      <span class="brand__dot"></span>
      <span class="brand__name">FrostLume Spa</span>
    </div>

    <div class="person">
      <p class="person__name">Your Long Name</p>
      <p class="person__title">Your Title</p>
    </div>

    <div class="contact">
      <div class="contact__row">
        <svg class="contact__icon" viewBox="0 0 24 24"><path d="M3 9c0-3 4-5 9-5s9 2 9 5l-4 1-1-3c-2-.6-6-.6-8 0l-1 3zM6 11h12l2 9H4z"/></svg>
        <span>(847) 555-0142</span>
      </div>
      <div class="contact__row">
        <svg class="contact__icon" viewBox="0 0 24 24"><path d="M2 5h20v14H2zM4 7v1l8 5 8-5V7l-8 5z"/></svg>
        <span>info@frostlumespa.com</span>
      </div>
      <div class="contact__row">
        <svg class="contact__icon" viewBox="0 0 24 24"><circle cx="12" cy="12" r="9" fill="none" stroke="var(--teal)" stroke-width="2"/><path d="M3 12h18M12 3c4 4 4 14 0 18M12 3c-4 4-4 14 0 18" fill="none" stroke="var(--teal)" stroke-width="1.6"/></svg>
        <span>www.frostlumespa.com</span>
      </div>
      <p class="contact__address">2210 Lakeview Road<br>Suite 204 Maple Grove, IL 60099</p>
    </div>

    <svg class="footer-band" width="711" height="22" viewBox="0 0 711 22" aria-hidden="true">
      <rect x="0" y="0" width="711" height="22" fill="var(--teal)"/>
      <polygon points="0,0 500,0 465,22 0,22" fill="var(--green)"/>
    </svg>
  </section>

</body>
</html>
```